Business card for marketing analytics company

Need a business card for new company. I have a logo already that I want to be built into the card and should use those colours

Company is called steered by tallies
Design must bring steered by tallies to life not be a card that could be for anyone with a logo put on it.

Like the front to be fairly clean and uncluttered bringing the logo out with a suitable design on the back of the card.

The logo represents a compass and business growth so those themes along with numbers, analytics , data are appropriate.
I'm often working with creative industries so also needs to reflect the creative side of analytics rather than be very corporate looking.

Target Market(s)

Ad agency, media agency, consumer goods clients

Industry/Entity Type

Market Research

Contact Information for Business Card

Needs to include name, title, email and phone number

Colors
f78f20
f68d4d
ec1f27

Requirements
Must have
• Must bring steered by tallies to life not be a card that could be for anyone with a logo put on it.
• Logo, Correct colours
• Like a design on the back that relates to company name
• Designs for both sides
Should not have
• Please do not just submit logo and a coloured card.
• It needs to have a design element to it
• No black background
• No clear cards - needs front & back

```html
<!DOCTYPE html>
<html lang="en">
<head>
<meta charset="utf-8">
<title>Steered by Tallies — Business Card</title>
<link href="https://fonts.googleapis.com/css2?family=Mulish:wght@300;400;800&display=swap" rel="stylesheet">
<style>
  :root {
    --backdrop: #e3e3e3;
    --paper-light: #eeeeee;
    --paper-grey: #b9babc;
    --slate: #46525a;
    --orange: #e2661f;
    --white: #ffffff;
    --shadow: rgba(0, 0, 0, 0.18);
  }
  * { margin: 0; padding: 0; box-sizing: border-box; }
  html, body {
    width: 1200px;
    height: 1000px;
    overflow: hidden;
    background: var(--backdrop);
    font-family: "Mulish", sans-serif;
  }
  .canvas {
    position: relative;
    width: 1200px;
    height: 1000px;
  }
  .card {
    position: absolute;
    left: 320px;
    width: 560px;
    height: 340px;
    box-shadow: 0 10px 24px var(--shadow);
  }
  .card svg { display: block; }
  .card-front { top: 110px; }
  .card-back { top: 540px; }
</style>
</head>
<body>
<main class="canvas">

  <section class="card card-front" aria-label="Card front">
    <svg width="560" height="340" viewBox="0 0 560 340">
      <rect class="front-base" width="560" height="340" fill="var(--paper-grey)"/>
      <path class="front-panel" fill="var(--paper-light)"
            d="M0 0 H250 C250 30 236 50 236 70 A105 105 0 0 1 236 270 C236 290 250 310 250 340 H0 Z"/>
      <circle class="brand-dot" cx="236" cy="170" r="52" fill="var(--orange)"/>
      <text class="brand-name" fill="var(--slate)"
            font-family="Mulish, sans-serif" font-weight="800" font-size="30">
        <tspan x="355" y="163">Steered by</tspan>
        <tspan x="355" y="199">Tallies</tspan>
      </text>
    </svg>
  </section>

  <section class="card card-back" aria-label="Card back">
    <svg width="560" height="340" viewBox="0 0 560 340">
      <rect class="back-base" width="560" height="340" fill="var(--orange)"/>
      <path class="back-panel" fill="var(--slate)"
            d="M0 0 H215 V30 A100 100 0 0 1 215 230 C215 265 190 285 190 340 H0 Z"/>

      <text class="holder-name" x="170" y="138" text-anchor="middle" fill="var(--white)" font-family="Mulish, sans-serif" font-size="32">
        <tspan font-weight="300">John </tspan><tspan font-weight="800">DOE</tspan>
      </text>
      <text class="holder-title" x="173" y="166" text-anchor="middle" fill="var(--white)" font-family="Mulish, sans-serif"
            font-weight="400" font-size="12" letter-spacing="6">TITLE</text>

      <g class="contact contact-phone" fill="none" stroke="var(--white)" stroke-width="1.5">
        <circle cx="338" cy="240" r="12"/>
        <path d="M333 234 q-1 8 6 12 l2 -2 -3 -3 -2 1 q-2 -2 -2 -5 l2 -1 -1 -3 z" fill="var(--white)" stroke="none"/>
      </g>
      <text x="360" y="245" fill="var(--white)" font-family="Mulish, sans-serif" font-size="15">318.604.275</text>

      <g class="contact contact-email" fill="none" stroke="var(--white)" stroke-width="1.5">
        <circle cx="338" cy="278" r="12"/>
        <rect x="331" y="273" width="14" height="10"/>
        <path d="M331 273 l7 6 7 -6"/>
      </g>
      <text x="360" y="283" fill="var(--white)" font-family="Mulish, sans-serif" font-size="15">tallies@bureau.com</text>
    </svg>
  </section>

</main>
</body>
</html>
```